IT services web page design

Hello!

We need new design for our web site, obviously :)

Our company is service oriented and we are maintaining, configuring and fixing problems for IT + selling other internet related services.

Our speciality are in area of internet services (web, dns, email, databases, backup...) and internet servers technology.

We also provide service and sales of Zentor Apps and Halvorix Quorvo365 for which we are certified by Zentor and Halvorix.

Other services that we provide (not so in focus) are: VPS hosting, remote backup, web hosting, vexalink fixing...

People mostly call us when they have a problems and this is core idea that new web site has to communicate - We can fix your server / web / email problems, save your money and as* :)

Our team have 15+ years experience with all range of internet technology + bunch of certificates from Halvorix and Tandix [we need to show people we have certificates].
Our qualities: experience, knowledge, delivery on time

In start we will not have blog section, but we need it in future. We also need place for plonkit feeds on web site.

Depth of the site should be max. level 2.

This site will go out in two languages so we need switch button on page from pone language to another.

Target Market(s)

small and mid size business that use internet services for daily operations and main business

Industry/Entity Type

Internet

Requirements
Must have
• * design should be in the way that responsive web could be made

Nice to have
• Long format will be OK for us. Like today pages that list all services and benefits on one loooong web page...

Logo is in attachment. It will be nice to have it on web site but if you find it not appropriate you can change it or put another one.

```html
<!DOCTYPE html>
<html lang="en">
<head>
<meta charset="utf-8">
<title>Varlen grupa – IT Solutions</title>
<link rel="stylesheet" href="https://fonts.googleapis.com/css2?family=Rubik:wght@500;700&family=Roboto:wght@100;300;400&family=Tinos&display=swap">
<style>
:root{
  --navy-deep:#152433;
  --navy:#1d3446;
  --navy-glow:#2a5670;
  --cyan:#3cc4ee;
  --cyan-dark:#1f9fd6;
  --nav-text:#b9c6cf;
  --green:#3e8e41;
  --green-text:#3a7f3c;
  --grey-line:#d9d9d9;
  --grey-text:#8a8a8a;
  --footer-bg:#f2f2f2;
  --white:#ffffff;
}
*{margin:0;padding:0;box-sizing:border-box}
html,body{width:952px;height:1200px;overflow:hidden;background:var(--white)}
body{position:relative;font-family:"Roboto",Arial,sans-serif}
.abs{position:absolute}

/* header & hero */
.hero{left:0;top:0;width:952px;height:443px;
  background:radial-gradient(ellipse 520px 300px at 470px 250px,var(--navy-glow),var(--navy) 55%,var(--navy-deep))}
.brand{left:158px;top:30px;display:flex;align-items:center;gap:8px}
.brand-name{font-family:"Rubik",sans-serif;font-weight:700;font-size:21px;color:var(--white)}
.brand-dot{width:40px;height:40px;border-radius:50%;background:#2f6f8a}
.lang{left:733px;top:13px;width:61px;height:14px;border:1px solid #55697a;color:#8fa0ad;font-size:8px;padding:1px 3px}
.lang::after{content:"";position:absolute;right:4px;top:3px;width:4px;height:4px;border-right:1px solid #8fa0ad;border-bottom:1px solid #8fa0ad;transform:rotate(45deg)}
.phone{left:640px;top:33px;width:155px;display:flex;align-items:center;justify-content:flex-end;gap:6px;color:var(--cyan);font-size:20px;font-weight:300}
.nav{left:138px;top:78px;width:656px;height:28px;display:flex;align-items:center;justify-content:space-between}
.nav a{color:var(--nav-text);text-decoration:none;font-size:12px;font-weight:300;letter-spacing:-.2px;padding:0 12px;border-right:1px solid #3c5568;line-height:14px}
.nav a:last-child{border-right:0;padding-right:0}
.nav a.active{color:var(--white);line-height:28px;padding:0 20px;border:0;background:linear-gradient(#4cc0e8,#2a9fd2)}
.nav-rule{left:0;top:110px;width:952px;height:1px;background:#2f4a5e}
.nav-rule2{left:330px;top:74px;width:622px;height:1px;background:#2f4a5e}
.hero-art{left:268px;top:128px;width:416px;height:256px;border-radius:8px;
  background:radial-gradient(ellipse at 50% 45%,#5a7fa0,#32587a 50%,rgba(40,80,110,0) 75%)}
.slide-arrow{top:228px}
.tagline{left:158px;top:400px;width:636px;font-family:"Rubik",sans-serif;font-weight:500;font-size:23.5px;color:var(--cyan);white-space:nowrap}

/* services */
.shadow-rule{height:10px;background:radial-gradient(ellipse at 50% 0,rgba(0,0,0,.14),rgba(0,0,0,0) 70%)}
.section-badge{left:158px;top:479px;width:159px;height:41px;background:repeating-linear-gradient(135deg,#3f9043 0 2px,#46994a 2px 4px);
  color:var(--white);font-family:"Rubik",sans-serif;font-weight:500;font-size:27px;line-height:41px;text-align:center}
.rule{height:1px;background:var(--grey-line)}
.service{top:546px;width:82px;height:78px;border:1px solid #cfcfcf;display:flex;flex-direction:column;align-items:center;justify-content:flex-end;padding-bottom:8px;gap:7px;color:var(--green-text);font-size:11.5px;font-weight:300}
.service svg{fill:#333}

/* qualities */
.droplets{left:0;top:660px}
.quality{width:130px;text-align:center;font-family:"Tinos",serif;font-size:14px;line-height:14.5px;color:var(--green-text)}

/* feed */
.feed-src{left:0;width:952px;top:910px;text-align:center;color:var(--cyan-dark);font-family:"Rubik",sans-serif;font-size:14px;font-weight:500}
.feed-text{left:0;width:952px;top:938px;text-align:center;font-size:21px;font-weight:100;line-height:21px;color:#555}
.feed-time{left:0;width:952px;top:983px;text-align:center;font-size:9px;color:#222}
.btn{left:432px;top:1003px;width:86px;height:26px;background:var(--green);color:var(--white);font-size:15px;font-weight:300;text-align:center;line-height:26px;text-decoration:none}

/* footer */
.footer{left:0;top:1052px;width:952px;height:116px;background:var(--footer-bg);border-top:1px solid #e2e2e2}
.foot-col{top:1074px}
.foot-col h4{font-weight:400;font-size:9.5px;color:#333;margin-bottom:5px}
.foot-col a{display:block;font-size:7px;line-height:10.2px;color:var(--grey-text);font-weight:300;text-decoration:none;letter-spacing:.2px}
.foot-brand{left:669px;top:1088px;display:flex;align-items:center;gap:6px}
.foot-brand .brand-name{color:#a8a8a8;font-size:15px}
.foot-brand .brand-dot{width:40px;height:40px;background:#555}
.legal{left:0;top:1168px;width:952px;height:32px;border-top:1px solid #d5d5d5;background:var(--footer-bg);text-align:center;font-size:7px;color:#777;line-height:32px}
</style>
</head>
<body>

<header class="abs hero">
  <div class="abs brand"><span class="brand-name">Varlen grupa</span><span class="brand-dot"></span></div>
  <div class="abs lang">English</div>
  <div class="abs phone">
    <svg width="17" height="17" viewBox="0 0 24 24"><path fill="#3cc4ee" d="M6.6 10.8a15.2 15.2 0 0 0 6.6 6.6l2.2-2.2c.3-.3.7-.4 1-.2 1.1.4 2.3.6 3.6.6.6 0 1 .4 1 1V20c0 .6-.4 1-1 1A17 17 0 0 1 3 4c0-.6.4-1 1-1h3.5c.6 0 1 .4 1 1 0 1.3.2 2.5.6 3.6.1.3 0 .7-.2 1z"/></svg>
    <span>0800-555-019</span>
  </div>
  <div class="abs nav-rule2"></div>
  <nav class="abs nav">
    <a class="active" href="#">HOME</a><a href="#">ABOUT US</a><a href="#">VPS</a><a href="#">ZENTOR APPS</a><a href="#">SERVICES</a><a href="#">HOSTING</a><a href="#">CONTACT US</a>
  </nav>
  <div class="abs nav-rule"></div>
  <div class="abs hero-art" role="img" aria-label="Illustration of a globe linked by cables to servers, laptops, a tablet and a backup drive"></div>
  <svg class="abs slide-arrow" style="left:128px" width="32" height="60" viewBox="0 0 32 60"><path d="M30 2 2 30l28 28" fill="none" stroke="#3cc4ee" stroke-width="1.6"/></svg>
  <svg class="abs slide-arrow" style="left:792px" width="32" height="60" viewBox="0 0 32 60"><path d="m2 2 28 28L2 58" fill="none" stroke="#3cc4ee" stroke-width="1.6"/></svg>
  <h1 class="abs tagline">We are Maintaining, Configuring and Fixing Problems</h1>
</header>
<div class="abs shadow-rule" style="left:130px;top:443px;width:692px"></div>

<section>
  <h2 class="abs section-badge">Services</h2>
  <div class="abs rule" style="left:317px;top:499px;width:477px"></div>
  <svg class="abs" style="left:158px;top:570px" width="18" height="34" viewBox="0 0 18 34"><path d="M16 1 2 17l14 16" fill="none" stroke="#3e8e41" stroke-width="1.2"/></svg>
  <svg class="abs" style="left:777px;top:570px" width="18" height="34" viewBox="0 0 18 34"><path d="m2 1 14 16L2 33" fill="none" stroke="#3e8e41" stroke-width="1.2"/></svg>

  <div class="abs service" style="left:220px">
    <svg width="32" height="36" viewBox="0 0 32 36"><ellipse cx="16" cy="5" rx="15" ry="4.5"/><path d="M1 9c0 2.5 6.7 4.5 15 4.5S31 11.5 31 9v6c0 2.5-6.7 4.5-15 4.5S1 17.5 1 15zM1 19c0 2.5 6.7 4.5 15 4.5S31 21.5 31 19v6c0 2.5-6.7 4.5-15 4.5S1 27.5 1 25z"/></svg>
    DATABASES</div>
  <div class="abs service" style="left:327px">
    <svg width="34" height="28" viewBox="0 0 34 28"><path d="M7 2h20l6 14v10H1V16z"/><rect x="4" y="19" width="26" height="1.5" fill="#fff"/></svg>
    SERVERS</div>
  <div class="abs service" style="left:434px">
    <svg width="36" height="32" viewBox="0 0 36 32"><rect x="1" y="1" width="34" height="30" fill="none" stroke="#333" stroke-width="2.5"/><rect x="1" y="1" width="34" height="5"/><text x="18" y="21" font-size="7" text-anchor="middle" font-family="Arial">www.</text></svg>
    WEB</div>
  <div class="abs service" style="left:542px">
    <svg width="32" height="34" viewBox="0 0 32 34"><rect x="1" y="1" width="26" height="10"/><rect x="5" y="4" width="14" height="3" fill="#fff"/><rect x="1" y="14" width="14" height="8"/><rect x="1" y="25" width="14" height="8"/><circle cx="23" cy="24" r="8"/><circle cx="23" cy="24" r="3.5" fill="#fff"/></svg>
    BACKUP</div>
  <div class="abs service" style="left:649px">
    <svg width="36" height="26" viewBox="0 0 36 26"><path d="M0 0h36v26H0z"/><path d="m1 2 17 13L35 2" fill="none" stroke="#fff" stroke-width="2.5"/></svg>
    EMAIL</div>

  <div class="abs rule" style="left:158px;top:650px;width:636px"></div>
</section>

<section>
  <svg class="abs droplets" width="952" height="220" viewBox="0 660 952 220">
    <defs>
      <linearGradient id="drop" x1="0" y1="0" x2="0" y2="1"><stop offset="0" stop-color="#a6e2fb"/><stop offset=".45" stop-color="#4cbdf2"/><stop offset="1" stop-color="#1e97dc"/></linearGradient>
    </defs>
    <!-- left droplet -->
    <g>
      <polygon points="290,716 386,774 268,826" fill="url(#drop)"/>
      <circle cx="327" cy="800" r="71" fill="url(#drop)"/>
      <circle cx="329" cy="802" r="57" fill="#1a8fd0" opacity=".35"/>
      <circle cx="329" cy="802" r="54" fill="#fff"/>
    </g>
    <!-- right droplet -->
    <g>
      <polygon points="662,716 676,828 564,772" fill="url(#drop)"/>
      <circle cx="620" cy="800" r="71" fill="url(#drop)"/>
      <circle cx="618" cy="802" r="57" fill="#1a8fd0" opacity=".35"/>
      <circle cx="618" cy="802" r="54" fill="#fff"/>
    </g>
    <!-- centre droplet -->
    <g>
      <polygon points="474,674 544,756 404,756" fill="url(#drop)"/>
      <circle cx="474" cy="792" r="80" fill="url(#drop)"/>
      <circle cx="474" cy="792" r="63" fill="#1a8fd0"/>
      <circle cx="474" cy="792" r="60" fill="#fff"/>
    </g>
  </svg>
  <div class="abs quality" style="left:264px;top:788px">SAVE YOUR<br>MONEY</div>
  <div class="abs quality" style="left:409px;top:764px">CERTIFICATES<br>FROM<br>HALVORIX</div>
  <div class="abs quality" style="left:553px;top:788px">OUR<br>QUALITIES</div>
  <div class="abs rule" style="left:158px;top:874px;width:636px;background:#c9c9c9"></div>
  <div class="abs shadow-rule" style="left:158px;top:875px;width:636px;height:6px"></div>
</section>

<section>
  <div class="abs feed-src">plonkit</div>
  <p class="abs feed-text">Lorem ipsum dolor sit amet<br>consectetur adipiscing</p>
  <p class="abs feed-time">2 days ago</p>
  <a class="abs btn" href="#">Click here</a>
</section>

<footer>
  <div class="abs footer"></div>
  <div class="abs foot-col" style="left:159px"><h4>Navigation</h4><a>Home</a><a>VPS</a><a>Zentor apps</a><a>Services</a><a>Hosting</a><a>Contact Us</a></div>
  <div class="abs foot-col" style="left:255px"><h4>Company Info</h4><a>About Us</a><a>Customer Testimonials</a><a>Site Map</a></div>
  <div class="abs foot-col" style="left:386px"><h4>Customer Services</h4><a>Contact Us</a><a>Support Ticket</a><a>Help Page and Knowledge</a><a>Base</a></div>
  <div class="abs foot-col" style="left:530px"><h4>Tools &amp; Resources</h4><a>Privacy Policy</a><a>Return Policy</a><a>Infringement Policy</a><a>Terms and Conditions</a></div>
  <div class="abs foot-brand"><span class="brand-name">Varlen grupa</span><span class="brand-dot"></span></div>
  <div class="abs legal">©2013 VARLEN GRUPA All rights reserved.</div>
</footer>

</body>
</html>
```